Brindle and Fern LLC | Land Clearing, Landscaping & Dump Trailer Services

Project Description: Brindle and Fern LLC Website Design
The website will be published using squarespace
Objective:
Design a visually compelling and conversion-driven website for Brindle and Fern LLC, a land solutions business based in Pickens County, Georgia. The site will highlight the company’s professionalism, locally rooted service, and commitment to quality in land clearing, grading, and dump trailer services.
Pages & Features to Include:
1. Landing Page (Homepage)
- Clear tagline: Sculpting Land with Precision and Power
- Call-to-Action (CTA) buttons: “Get a Free Quote” and “View Services”
- Service highlights with icons or photos (e.g., grading, mulching, hauling)
- Customer testimonials
- Embedded contact form
- Google Maps integration showing service area
2. Services + Pricing Page
- Organized list of services under 3 categories:
- **Land Clearing & Grading**
- Forestry Mulching
- Gravel Driveway Repair
- Minimum Job Fee:
- Dump Trailer Services
- Trailer Rental (Daily):
- Junk Removal (Full Load)
- Material Delivery: $ + mileage
- Specialty Jobs
- Stump removal, light demolition
- Each service section includes short descriptions and photos
- Optional quote form at the bottom with “Request a Quote” CTA
Design Style:
- Clean, professional design using clean tones
- Fonts that balance industrial strength and local charm
- Mobile-optimized with fast loading speeds and easy navigation
- SEO-optimized for terms like *land clearing Pickens County*, *grading services North Georgia*, and *dump trailer rental Jasper GA*, etc...

```html
<!DOCTYPE html>
<html lang="en">
<head>
<meta charset="utf-8">
<title>Brindle and Fern LLC | Land Clearing, Grading &amp; Dump Trailer Services</title>
<link rel="stylesheet" href="https://fonts.googleapis.com/css2?family=Roboto:wght@400;500;700;900&display=swap">
<style>
:root{
  --red:#e03e25;
  --yellow:#fbb934;
  --dark:#151515;
  --ink:#1d1d1d;
  --grey:#e7e7e7;
  --card-grey:#d8d8d8;
  --muted:#555;
  --white:#fff;
}
*{box-sizing:border-box;margin:0;padding:0}
html,body{width:1200px;height:4743px;overflow:hidden}
body{position:relative;font-family:"Roboto",Arial,sans-serif;color:var(--ink);background:var(--white)}
.abs{position:absolute}
.btn{position:absolute;display:flex;align-items:center;justify-content:center;font-weight:500;font-size:16px;text-transform:uppercase;border-radius:4px;letter-spacing:.2px;white-space:nowrap}
.btn-yellow{background:var(--yellow);color:var(--ink)}
.btn-outline{border:2px solid var(--white);color:var(--white)}
.section-title{position:absolute;left:0;width:1200px;text-align:center;font-size:38px;font-weight:500}
.underline{position:absolute;height:4px;width:54px;background:var(--red)}

/* header */
.topbar-tab{left:0;top:0;width:304px;height:26px;background:var(--red);clip-path:polygon(0 0,100% 0,90% 100%,0 100%)}
.social-dot{position:absolute;top:7px;width:12px;height:12px;border-radius:50%;background:var(--white)}
.nav a{position:absolute;top:43px;font-size:16px;color:var(--ink);text-decoration:none}
.nav a::after{content:"";display:inline-block;width:5px;height:5px;background:currentColor;margin-left:7px;vertical-align:middle}
.nav a.active{color:var(--red)}
.brand-badge{left:514px;top:18px;width:172px;height:172px;border-radius:50%;background:var(--white);z-index:5;display:flex;align-items:center;justify-content:center;text-align:center;font-weight:700;font-size:19px;line-height:1.2;color:var(--ink);padding:0 22px}
.tollfree{left:924px;top:18px}
.tollfree .ring{position:absolute;left:0;top:4px;width:32px;height:32px;border:2px solid var(--red);border-radius:50%;display:flex;align-items:center;justify-content:center}
.tollfree small{position:absolute;left:46px;top:0;font-size:13px;white-space:nowrap;color:var(--muted)}
.tollfree strong{position:absolute;left:46px;top:17px;font-size:19px;white-space:nowrap;letter-spacing:.5px}

/* hero */
.hero{left:0;top:74px;width:1200px;height:740px}
.hero-title{left:0;top:260px;width:1200px;text-align:center;color:var(--white);font-size:56px;font-weight:700;line-height:62px}

/* service cards */
.svc-card{position:absolute;top:953px;width:311px;height:436px;background:var(--card-grey);overflow:hidden;border-radius:3px}
.svc-card.featured{background:var(--red);color:var(--white)}
.svc-card svg.photo{position:absolute;left:0;top:0}
.svc-icon{position:absolute;left:24px;top:243px;width:74px;height:74px;border-radius:50%;background:var(--red);border:4px solid rgba(255,255,255,.7);display:flex;align-items:center;justify-content:center}
.featured .svc-icon{background:var(--yellow)}
.svc-card h3{position:absolute;left:28px;top:318px;font-size:28px;font-weight:500;white-space:nowrap}
.svc-card p{position:absolute;left:28px;top:355px;width:260px;font-size:13.5px;line-height:18px;color:#444}
.featured p{color:var(--white)}
.svc-card .link{position:absolute;left:30px;top:398px;font-size:15px;font-weight:700;text-decoration:underline}

/* welcome */
.welcome{left:0;top:1536px;width:1200px;height:770px;background:var(--dark)}
.welcome-title{left:105px;top:1624px;color:var(--white);font-size:40px;font-weight:500;line-height:46px}
.welcome-copy{left:105px;top:1745px;width:435px;color:#ddd;font-size:13.5px;line-height:22px}
.feature-icon{position:absolute;width:68px;height:68px;border-radius:50%;background:var(--yellow);display:flex;align-items:center;justify-content:center}
.feature h4{position:absolute;left:192px;font-size:19px;font-weight:500;color:var(--white)}
.feature p{position:absolute;left:192px;width:300px;font-size:13.5px;line-height:21px;color:#ddd}

/* testimonials */
.testi-card{position:absolute;top:2455px;width:311px;height:278px;background:var(--white);border-radius:4px;overflow:hidden}
.testi-card.featured{background:var(--red);color:var(--white)}
.avatar{position:absolute;left:20px;top:25px;width:74px;height:74px;border-radius:50%;border:4px solid var(--white);background:linear-gradient(150deg,#d9c2a8,#8d6e55)}
.testi-card .name{position:absolute;left:106px;top:36px;font-size:16px;font-weight:500}
.testi-card .role{position:absolute;left:106px;top:58px;font-size:13px}
.testi-card .stars{position:absolute;left:106px;top:74px;font-size:14px;letter-spacing:1px;color:var(--red)}
.testi-card.featured .stars{color:var(--white)}
.testi-card blockquote{position:absolute;left:20px;top:120px;width:275px;font-size:13.5px;line-height:22px;color:#333}
.testi-card.featured blockquote{color:var(--white)}
.quote-mark{position:absolute;right:18px;bottom:6px;width:36px;height:26px}

/* contact */
.contact-title{left:105px;top:3026px;font-size:40px;font-weight:500;line-height:46px}
.contact-copy{left:105px;top:3163px;width:340px;font-size:13.5px;line-height:22px;color:#444}
.contact-icon{position:absolute;left:106px;width:54px;height:54px;border-radius:50%;background:var(--yellow);display:flex;align-items:center;justify-content:center}
.contact-line{position:absolute;left:181px;font-size:16px;line-height:23px}
.quote-form{left:491px;top:2966px;width:591px;height:488px;background:var(--red);color:var(--white)}
.quote-form h2{position:absolute;left:32px;top:28px;font-size:38px;font-weight:700}
.field-label{position:absolute;font-size:13px;font-weight:500;text-transform:uppercase}
.field{position:absolute;background:var(--white);border:1px solid #ccc;color:#555;font:13px "Roboto",Arial,sans-serif;padding:0 9px;display:flex;align-items:center;white-space:nowrap}
.field.area{align-items:flex-start;padding-top:10px}

/* area */
.area{left:0;top:3625px;width:1200px;height:720px;background:#f6f6f6}
.map-label{position:absolute;background:var(--dark);color:var(--white);font-size:13px;padding:3px 8px;white-space:nowrap}
.pin{position:absolute;width:20px;height:20px;border-radius:50%;border:3px solid var(--red);background:var(--white)}
.pin::after{content:"";position:absolute;left:4px;top:4px;width:6px;height:6px;border-radius:50%;background:var(--red)}

/* footer */
.footer{left:0;top:4300px;width:1200px;height:443px;background:var(--dark);clip-path:polygon(0 25px,100% 0,100% 100%,0 100%)}
.footer-head{font-size:14px;font-weight:700;color:var(--white);text-transform:uppercase}
.footer-item{font-size:13px;color:#ccc;white-space:nowrap}
.footer-brand{left:105px;top:4384px;width:94px;height:94px;border-radius:50%;background:var(--white);display:flex;align-items:center;justify-content:center;text-align:center;font-size:12px;font-weight:700;color:var(--ink);line-height:1.2;padding:0 8px}
.news-input{left:784px;top:4497px;width:296px;height:48px;background:var(--white);color:#444;font-size:15px;display:flex;align-items:center;padding-left:18px}
.news-send{left:1008px;top:4497px;width:72px;height:48px;background:var(--yellow);clip-path:polygon(16% 0,100% 0,100% 100%,0 100%);display:flex;align-items:center;justify-content:center}
.bottom-band{left:562px;top:4665px;width:638px;height:78px;background:#2b2b2b;clip-path:polygon(8% 0,100% 0,100% 100%,0 100%)}
.band-icon{position:absolute;width:32px;height:32px;border-radius:50%;background:var(--red);display:flex;align-items:center;justify-content:center}
.band-text{position:absolute;font-size:12.5px;line-height:18px;color:#aaa;white-space:nowrap}
.band-text b{color:var(--white);font-weight:500}
</style>
</head>
<body>

<!-- Header -->
<div class="abs topbar-tab" aria-label="Social links">
  <span class="social-dot" style="left:104px"></span>
  <span class="social-dot" style="left:140px"></span>
  <span class="social-dot" style="left:176px"></span>
  <span class="social-dot" style="left:222px"></span>
</div>
<nav class="nav">
  <a class="active" style="left:105px">Home</a>
  <a style="left:219px">Services</a>
  <a style="left:351px">Contact</a>
</nav>
<div class="abs brand-badge">Brindle and Fern LLC</div>
<div class="abs tollfree">
  <span class="ring"><svg width="16" height="16" viewBox="0 0 24 24"><path fill="#e03e25" d="M6.6 10.8a15.1 15.1 0 0 0 6.6 6.6l2.2-2.2c.3-.3.7-.4 1-.2 1.1.4 2.3.6 3.6.6.6 0 1 .4 1 1V20c0 .6-.4 1-1 1A17 17 0 0 1 3 4c0-.6.4-1 1-1h3.5c.6 0 1 .4 1 1 0 1.3.2 2.5.6 3.6.1.3 0 .7-.2 1z"/></svg></span>
  <small>Toll Free Number</small>
  <strong>123-555-0147</strong>
</div>

<!-- Hero -->
<svg class="abs hero" viewBox="0 0 1200 740" role="img" aria-label="Three photos of crews clearing woodland: a worker with a leaf blower, a compact track loader among trees, and an arborist cutting branches">
  <defs>
    <linearGradient id="heroLeft" x1="0" y1="0" x2="0" y2="1"><stop offset="0" stop-color="#3d3a30"/><stop offset="1" stop-color="#6d5a3a"/></linearGradient>
    <linearGradient id="heroMid" x1="0" y1="0" x2="0" y2="1"><stop offset="0" stop-color="#2c2d27"/><stop offset="1" stop-color="#3b4330"/></linearGradient>
    <linearGradient id="heroRight" x1="0" y1="0" x2="0" y2="1"><stop offset="0" stop-color="#3a3a2a"/><stop offset="1" stop-color="#4f4f2e"/></linearGradient>
  </defs>
  <polygon points="0,0 1200,0 1200,64 600,736 0,64" fill="url(#heroMid)"/>
  <polygon points="0,64 600,736 497,634 0,708" fill="url(#heroLeft)"/>
  <polygon points="1200,64 600,736 700,634 1200,716" fill="url(#heroRight)"/>
  <line x1="0" y1="64" x2="600" y2="736" stroke="#fff" stroke-width="3"/>
  <line x1="1200" y1="64" x2="600" y2="736" stroke="#fff" stroke-width="3"/>
</svg>
<h1 class="abs hero-title">Sculpting Land With<br>Precision And Power</h1>
<a class="btn btn-yellow" style="left:394px;top:414px;width:189px;height:54px">Get A Free Quote</a>
<a class="btn btn-outline" style="left:598px;top:414px;width:188px;height:54px">View Services</a>

<!-- Services -->
<h2 class="section-title" style="top:862px">Our Services</h2>
<span class="underline abs" style="left:573px;top:910px"></span>

<article class="svc-card" style="left:105px">
  <svg class="photo" width="311" height="436" role="img" aria-label="Worker trimming grass with a brush cutter in a park">
    <defs><linearGradient id="g1" x1="0" y1="0" x2="0" y2="1"><stop offset="0" stop-color="#b9c4b0"/><stop offset="1" stop-color="#5f8a3b"/></linearGradient></defs>
    <polygon points="0,0 311,0 311,353 0,261" fill="url(#g1)"/>
    <polygon points="0,261 311,353 311,365 0,273" fill="#fff"/>
  </svg>
  <span class="svc-icon"><svg width="34" height="34" viewBox="0 0 24 24"><path fill="#fff" d="M12 2 5 12h4l-3 5h5v5h2v-5h5l-3-5h4z"/></svg></span>
  <h3>Land Clearing</h3>
  <p>Lorem Ipsum has been the industry's standard dummy</p>
  <span class="link">GET A QUOTE</span>
</article>

<article class="svc-card featured" style="left:442px">
  <svg class="photo" width="311" height="436" role="img" aria-label="Gloved hand pruning a branch with yellow-handled shears">
    <defs><linearGradient id="g2" x1="0" y1="0" x2="1" y2="1"><stop offset="0" stop-color="#7a2a1c"/><stop offset="1" stop-color="#3c3f2c"/></linearGradient></defs>
    <polygon points="0,0 311,0 311,353 0,261" fill="url(#g2)"/>
    <polygon points="0,261 311,353 311,365 0,273" fill="#fff"/>
  </svg>
  <span class="svc-icon"><svg width="36" height="36" viewBox="0 0 24 24"><path fill="#1d1d1d" d="M2 9h13l-2 6H6zM15 9l3-4h3v2h-2l-3 4zM8 16a2.5 2.5 0 1 1 0 5 2.5 2.5 0 0 1 0-5z"/></svg></span>
  <h3>Land Grading</h3>
  <p>Lorem Ipsum has been the industry's standard dummy</p>
  <span class="link">GET A QUOTE</span>
</article>

<article class="svc-card" style="left:780px">
  <svg class="photo" width="311" height="436" role="img" aria-label="Waste truck lifting a blue dumpster beside houses">
    <defs><linearGradient id="g3" x1="0" y1="0" x2="0" y2="1"><stop offset="0" stop-color="#9fb7c9"/><stop offset="1" stop-color="#3e4f73"/></linearGradient></defs>
    <polygon points="0,0 311,0 311,353 0,261" fill="url(#g3)"/>
    <polygon points="0,261 311,353 311,365 0,273" fill="#fff"/>
  </svg>
  <span class="svc-icon"><svg width="36" height="36" viewBox="0 0 24 24"><path fill="#fff" d="M1 7h13v9H1zM14 10h4l4 4v2h-8zM5 16a2 2 0 1 1 0 4 2 2 0 0 1 0-4zm12 0a2 2 0 1 1 0 4 2 2 0 0 1 0-4z"/></svg></span>
  <h3>Dump Trailer</h3>
  <p>Lorem Ipsum has been the industry's standard dummy</p>
  <span class="link">GET A QUOTE</span>
</article>

<a class="btn btn-yellow" style="left:504px;top:1420px;width:192px;height:54px">View All Services</a>

<!-- Welcome -->
<section class="abs welcome"></section>
<svg class="abs" style="left:0;top:2190px" width="1200" height="120" aria-hidden="true"><polygon points="0,110 1200,0 1200,120 0,120" fill="#e7e7e7"/></svg>
<h2 class="abs welcome-title">Welcome To Brindle<br>And Fern LLC</h2>
<span class="underline abs" style="left:105px;top:1719px"></span>
<p class="abs welcome-copy">Lorem Ipsum has been the industry's standard dummy text ever since the 1500s, when an unknown printer took a galley of type and scrambled it to make a type specimen book. It has survived not only five centuries,</p>

<div class="feature">
  <span class="feature-icon" style="left:104px;top:1852px"><svg width="34" height="34" viewBox="0 0 24 24"><path fill="#e03e25" d="M6 2v8a2 2 0 0 0 2 2v10h2V12a2 2 0 0 0 2-2V2h-1.5v6h-1V2h-1v6h-1V2zm11 0c-2 0-3 3-3 6v5h2v9h2V2z"/></svg></span>
  <h4 style="top:1854px">Locally rooted service</h4>
  <p style="top:1882px">Lorem Ipsum is simply dummy text of the printing and typesetting industry.</p>
</div>
<div class="feature">
  <span class="feature-icon" style="left:104px;top:1948px"><svg width="34" height="34" viewBox="0 0 24 24"><circle cx="12" cy="12" r="10" fill="#e03e25"/><path d="m7 12 3.5 3.5L17 9" stroke="#fbb934" stroke-width="2.4" fill="none"/></svg></span>
  <h4 style="top:1948px">Commitment to quality</h4>
  <p style="top:1976px">Lorem Ipsum is simply dummy text of the printing and typesetting industry.</p>
</div>
<a class="btn btn-yellow" style="left:105px;top:2057px;width:189px;height:54px">Get A Free Quote</a>
<a class="btn btn-outline" style="left:307px;top:2057px;width:190px;height:54px">View Services</a>

<svg class="abs" style="left:576px;top:1647px" width="60" height="60" aria-hidden="true"><path d="M0 0h60v15H15v45H0z" fill="#e03e25"/></svg>
<div class="abs" style="left:591px;top:1662px;width:320px;height:381px;background:linear-gradient(160deg,#3b4a2d,#7a6a4c 60%,#2f3a25)" role="img" aria-label="Smiling landscaper in an apron holding pruning shears"></div>
<svg class="abs" style="left:817px;top:2043px" width="60" height="73" aria-hidden="true"><path d="M0 0h15v58h45v15H0z" fill="#e03e25"/></svg>
<div class="abs" style="left:828px;top:1778px;width:272px;height:323px;background:#fff;padding:8px">
  <div style="width:100%;height:100%;background:linear-gradient(180deg,#a7b9c8,#6f8a6a 55%,#2f8a4a)" role="img" aria-label="Crew loading brush into a green dump truck by a mountain"></div>
</div>

<!-- Testimonials -->
<div class="abs" style="left:0;top:2300px;width:1200px;height:570px;background:var(--grey)"></div>
<h2 class="section-title" style="top:2336px">Client Testimonial</h2>
<span class="underline abs" style="left:573px;top:2396px"></span>

<article class="testi-card" style="left:105px">
  <svg class="abs" style="left:0;top:0" width="311" height="90" aria-hidden="true"><path d="M0 0H240Q120 12 0 70Z" fill="#fbb934"/></svg>
  <span class="avatar" role="img" aria-label="Customer portrait"></span>
  <span class="name">JAMES HOLDERS</span>
  <span class="role">Our Customer</span>
  <span class="stars">★★★★★</span>
  <blockquote>“ Lorem Ipsum has been the industry's standard dummy text ever since the 1500s, when an unknown printer took a galley of type and scrambled it to make a type specimen book. ”</blockquote>
  <svg class="quote-mark" viewBox="0 0 36 26" aria-hidden="true"><path fill="#d5d5d5" d="M0 0h14v14l-6 12H2l5-11H0zM20 0h14v14l-6 12h-6l5-11h-7z"/></svg>
</article>
<article class="testi-card featured" style="left:444px">
  <svg class="abs" style="left:0;top:0" width="311" height="90" aria-hidden="true"><path d="M0 0H240Q120 12 0 70Z" fill="#fbb934"/></svg>
  <span class="avatar" role="img" aria-label="Customer portrait"></span>
  <span class="name">JOHN DOE</span>
  <span class="role">Our Customer</span>
  <span class="stars">★★★★★</span>
  <blockquote>“ Lorem Ipsum has been the industry's standard dummy text ever since the 1500s, when an unknown printer took a galley of type and scrambled it to make a type specimen book. ”</blockquote>
  <svg class="quote-mark" viewBox="0 0 36 26" aria-hidden="true"><path fill="rgba(255,255,255,.4)" d="M0 0h14v14l-6 12H2l5-11H0zM20 0h14v14l-6 12h-6l5-11h-7z"/></svg>
</article>
<article class="testi-card" style="left:784px">
  <svg class="abs" style="left:0;top:0" width="311" height="90" aria-hidden="true"><path d="M0 0H240Q120 12 0 70Z" fill="#fbb934"/></svg>
  <span class="avatar" role="img" aria-label="Customer portrait"></span>
  <span class="name">JAMES HOLDERS</span>
  <span class="role">Our Customer</span>
  <span class="stars">★★★★★</span>
  <blockquote>“ Lorem Ipsum has been the industry's standard dummy text ever since the 1500s, when an unknown printer took a galley of type and scrambled it to make a type specimen book. ”</blockquote>
  <svg class="quote-mark" viewBox="0 0 36 26" aria-hidden="true"><path fill="#d5d5d5" d="M0 0h14v14l-6 12H2l5-11H0zM20 0h14v14l-6 12h-6l5-11h-7z"/></svg>
</article>
<svg class="abs" style="left:64px;top:2582px" width="16" height="24" aria-label="Previous"><path d="M13 2 3 12l10 10" stroke="#e03e25" stroke-width="3" fill="none"/></svg>
<svg class="abs" style="left:1112px;top:2582px" width="16" height="24" aria-label="Next"><path d="m3 2 10 10L3 22" stroke="#e03e25" stroke-width="3" fill="none"/></svg>

<!-- Contact -->
<h2 class="abs contact-title">Get In Touch<br>With Us</h2>
<p class="abs contact-copy">Lorem Ipsum has been the industry's standard dummy text ever since the 1500s, when an unknown printer took a galley of type</p>
<span class="contact-icon" style="top:3270px"><svg width="22" height="22" viewBox="0 0 24 24"><path fill="#1d1d1d" d="M6.6 10.8a15.1 15.1 0 0 0 6.6 6.6l2.2-2.2c.3-.3.7-.4 1-.2 1.1.4 2.3.6 3.6.6.6 0 1 .4 1 1V20c0 .6-.4 1-1 1A17 17 0 0 1 3 4c0-.6.4-1 1-1h3.5c.6 0 1 .4 1 1 0 1.3.2 2.5.6 3.6.1.3 0 .7-.2 1z"/></svg></span>
<div class="contact-line" style="top:3274px">Toll Free<br><b>(+45) 555-010-2290</b></div>
<span class="contact-icon" style="top:3351px"><svg width="22" height="22" viewBox="0 0 24 24"><path fill="#1d1d1d" d="M3 5h18v14H3zm2 2v.5l7 5 7-5V7z"/></svg></span>
<div class="contact-line" style="top:3357px">Email Us At:<br><b>hello@brindlefern.com</b></div>

<div class="abs" style="left:484px;top:2958px;width:320px;height:200px;background:var(--yellow)"></div>
<div class="abs" style="left:780px;top:3330px;width:310px;height:132px;background:var(--yellow)"></div>
<form class="abs quote-form">
  <h2>Get A Quote</h2>
  <span class="field-label" style="left:34px;top:98px">Name</span>
  <span class="field" style="left:32px;top:118px;width:246px;height:37px">Your First &amp; Last Name</span>
  <span class="field-label" style="left:308px;top:98px">Email</span>
  <span class="field" style="left:306px;top:118px;width:245px;height:37px">example@yourmail.com</span>
  <span class="field-label" style="left:34px;top:181px">Phone</span>
  <span class="field" style="left:32px;top:199px;width:246px;height:37px">+1</span>
  <span class="field-label" style="left:308px;top:181px">Services</span>
  <span class="field" style="left:306px;top:199px;width:245px;height:37px;justify-content:space-between">Which service do you need? <svg width="12" height="8"><path d="m1 1 5 5 5-5" stroke="#333" stroke-width="2" fill="none"/></svg></span>
  <span class="field-label" style="left:34px;top:256px">Message</span>
  <span class="field area" style="left:32px;top:274px;width:519px;height:105px">Tell us what you'd like to talk to us about</span>
  <span class="btn btn-yellow" style="left:32px;top:396px;width:191px;height:55px">Submit Now</span>
</form>

<!-- Service area -->
<section class="abs area"></section>
<h2 class="section-title" style="top:3696px">Our Services Area</h2>
<span class="underline abs" style="left:573px;top:3752px"></span>
<div class="abs" style="left:110px;top:3760px;width:976px;height:430px;border-radius:40% 30% 45% 35%;background:radial-gradient(ellipse at center,#d4d4d4,#e9e9e9 70%,#f6f6f6)" role="img" aria-label="Dotted map of the Pickens County service region"></div>
<span class="map-label" style="left:363px;top:3840px">Lorem ipsum</span><span class="pin" style="left:351px;top:3873px"></span>
<span class="map-label" style="left:423px;top:3910px">Lorem ipsum</span><span class="pin" style="left:411px;top:3940px"></span>
<span class="map-label" style="left:407px;top:3986px">Lorem ipsum</span><span class="pin" style="left:397px;top:4018px"></span>
<span class="map-label" style="left:570px;top:3988px">Lorem ipsum</span><span class="pin" style="left:560px;top:4018px"></span>
<span class="map-label" style="left:716px;top:3952px">Lorem ipsum</span><span class="pin" style="left:706px;top:3983px"></span>
<span class="map-label" style="left:863px;top:3986px">Lorem ipsum</span><span class="pin" style="left:853px;top:4018px"></span>

<!-- Footer -->
<footer class="abs footer"></footer>
<div class="abs footer-brand">Brindle and Fern LLC</div>
<span class="social-dot" style="top:4506px;left:106px"></span>
<span class="social-dot" style="top:4506px;left:134px"></span>
<span class="social-dot" style="top:4506px;left:164px"></span>
<span class="social-dot" style="top:4506px;left:195px"></span>

<h5 class="abs footer-head" style="left:269px;top:4388px">Land Clearing</h5>
<span class="abs footer-item" style="left:269px;top:4441px">Forestry Mulching</span>
<span class="abs footer-item" style="left:269px;top:4474px">Gravel Driveway Repair</span>
<h5 class="abs footer-head" style="left:269px;top:4518px">Land Grading</h5>
<span class="abs footer-item" style="left:269px;top:4572px">Forestry Mulching</span>
<span class="abs footer-item" style="left:269px;top:4605px">Gravel Driveway Repair</span>
<h5 class="abs footer-head" style="left:500px;top:4388px">Dump Trailer</h5>
<span class="abs footer-item" style="left:500px;top:4439px">Trailer Rental (Daily)</span>
<span class="abs footer-item" style="left:500px;top:4472px">Junk Removal (Full Load)</span>
<span class="abs footer-item" style="left:500px;top:4505px">Stump removal, light demolition</span>
<h5 class="abs footer-head" style="left:784px;top:4388px">Sign Up Newsletter</h5>
<span class="abs" style="left:784px;top:4436px;font-size:13px;line-height:26px;width:260px;color:#ccc">Subscribe Our Newsletter To Get Our latest updates &amp; news</span>
<div class="abs news-input">Instant Quote</div>
<div class="abs news-send"><svg width="26" height="26" viewBox="0 0 24 24"><path fill="#1d1d1d" d="M22 2 2 10l7 3 3 7zM9 13l9-9"/><path d="M9 13 20 4" stroke="#fbb934" stroke-width="1.5"/></svg></div>

<p class="abs" style="left:105px;top:4693px;font-size:13px;color:#ccc;white-space:nowrap">Copyright © 2025 <span style="color:var(--red)">BRINDLE AND FERN LLC</span>, ALL RIGHT RESERVED</p>
<div class="abs bottom-band"></div>
<span class="band-icon" style="left:632px;top:4691px"><svg width="16" height="16" viewBox="0 0 24 24"><path fill="#fff" d="M12 3 2 12h3v8h5v-6h4v6h5v-8h3z"/></svg></span>
<span class="band-text" style="left:677px;top:4683px">Address :<br><b>18 Orchard Row, Jasper GA 30143</b></span>
<span class="band-icon" style="left:915px;top:4691px"><svg width="16" height="16" viewBox="0 0 24 24"><path fill="#fff" d="M3 5h18v14H3zm2 2v.5l7 5 7-5V7z"/></svg></span>
<span class="band-text" style="left:962px;top:4683px">Email :<br><b>hello@brindlefern.com</b></span>

</body>
</html>
```